Website for Franchise Builder

We are a web design and Architectural company that is selling an all in one Business solution for small to medium size builders.

We are Frame KV..

We are providing builders with the following services:

1. Dynamic Site quarry websites and Zentap Apps
2. Rebranded housed plans with Brochures
3. Logo and Corporate identity
4. Estimating software
5. 3d Visualisation and Rendering
5. Building design and Planning support.

We will be helping builders to complete and have a competitive edge against the large franchise building companies. Who control the House building market in Australia. The large companies have great website, apps, brochures and standard house plans. So that is exactly what we will be providing our builders. At a fraction of the normal cost. We will have help them to win jobs and look more professional.

My current website is:

http://norvellpage.sitequarry.com

I have attached and provided the following:

1. whole website Mock-up
2. Separated competition Pages to mock-up
2. Logo (in latest advertisement zip file)
4. Images and that my be useful
5. Some information on our services
6. Latest magazine advertisement (notice the ad also displays the roofdraftguild. Which is a separate website that sells our house plans)

The five pages i would like designed for the competition are follows:

1. Home Page
2. What we do - Websites & Zentap Apps
3. How it works
4. Our work - Display individual websites similar to the way www.plomarex.com displays their websites
5. Builders packages (pricing table. Mockup has incorrect items for table. See please pdf with correct data for table)

Please use the mock-ups as a guide only. Go for it with your creativity please.

Sites that i really like are:

- www.plomarex.com
- www.quillmarket.com.au

Target Market(s)

Builders and Wifes of Builders

Industry/Entity Type

Business

Requirements
Must have
• 1. Testimonails displayed on home page somewhere
2. Social media on home page, and on individual pages displaying websites

Nice to have
• I really like the www.plomarex.com. The way they use icons and have the catch phrases. We could have catch phase such as:

1. All in one Business Solution for builders
2. Lets Get Started View websites
3. Ready to Go Business Solutions for Builders.

```html
<!DOCTYPE html>
<html lang="en">
<head>
<meta charset="utf-8">
<title>Frame KV — All in one Business Solutions for Builders</title>
<link rel="stylesheet" href="https://fonts.googleapis.com/css2?family=Arimo:ital,wght@0,400;0,700;1,400&family=Gelasio:ital@1&display=swap">
<style>
:root{
  --brand-blue:#1a7cc4;
  --brand-sky:#5bb8e6;
  --ink:#1d1d1d;
  --body-text:#8a8a8a;
  --nav-bg:#1f1f1f;
  --nav-line:#444;
  --page-bg:#ffffff;
  --grid-bg:#f1f1f1;
  --hero-top:#f4f8fc;
  --hero-bottom:#dce9f5;
  --rule-blue:#2d84c8;
  --link-blue:#1f73b8;
  --accent-orange:#e3622a;
  --footer-bg:#151515;
}
*{box-sizing:border-box;margin:0;padding:0}
html,body{width:1200px;height:2239px;overflow:hidden}
body{position:relative;background:var(--page-bg);font-family:"Arimo",Arial,sans-serif;color:var(--ink)}
.abs{position:absolute}

/* header */
.site-header{left:0;top:0;width:1200px;height:190px;background:linear-gradient(#fff,#f4f4f4)}
.brand{left:119px;top:78px;display:flex;align-items:center;gap:12px}
.brand-mark{width:36px;height:36px;border-radius:50%;background:var(--brand-sky)}
.brand-name{font-size:40px;font-weight:700;color:var(--brand-blue);letter-spacing:-1px}
.util-links{right:240px;top:35px;display:flex;font-size:13px}
.util-links a{color:var(--ink);text-decoration:none;padding:0 12px;border-left:1px solid #999;line-height:16px}
.util-links a:first-child{border-left:none}
.util-links a:last-child{padding-right:0}
.social{right:116px;top:26px;display:flex;gap:12px}
.social span{width:28px;height:28px;border-radius:50%;background:#6d8aa8;display:block}
.call{right:116px;top:82px;display:flex;align-items:center;gap:8px;font-weight:700}
.call-label{font-size:18px}
.call-number{font-size:22px}
.search{left:901px;top:133px;width:183px;height:33px;background:#151515;border:1px solid #666;border-radius:2px;color:var(--brand-sky);font-size:12px;font-weight:700;padding:9px 10px}
.search svg{position:absolute;right:10px;top:9px}

/* nav */
.main-nav{left:0;top:190px;width:1200px;height:38px;background:var(--nav-bg);display:flex;padding-left:119px}
.main-nav a{color:#fff;font-size:14px;font-weight:700;text-decoration:none;display:flex;align-items:center;justify-content:center;border-right:1px solid var(--nav-line);height:38px}

/* hero */
.hero{left:0;top:228px;width:1200px;height:356px;background:linear-gradient(var(--hero-top),var(--hero-bottom));border-bottom:2px solid var(--rule-blue)}
.shot{box-shadow:0 4px 10px rgba(0,0,0,.25)}
.hero-title{left:764px;top:82px;font-size:27px;font-weight:700;line-height:32px}
.hero-copy{left:765px;top:152px;width:250px;font-size:12.5px;line-height:16px;color:var(--body-text)}
.btn-learn{left:765px;top:232px;width:86px;height:30px;border-radius:4px;background:linear-gradient(#3a8fd6,#1459a3);color:#fff;font-size:12px;font-weight:700;display:flex;align-items:center;justify-content:center;border:1px solid #0e3f78}
.dots{left:963px;top:317px;display:flex;gap:4px}
.dots span{width:8px;height:8px;border-radius:50%;background:#b9c3cc}
.dots span.on{background:#39434d}

/* intro */
.intro{left:0;top:584px;width:1200px;height:120px;background:#fafafa;border-bottom:2px solid var(--rule-blue)}
.intro h2{position:absolute;left:121px;top:24px;font-size:25px;color:var(--brand-blue)}
.intro p{position:absolute;left:122px;top:62px;width:960px;font-size:13px;line-height:18px;color:#333}

/* services grid */
.services{left:0;top:704px;width:1200px;height:1124px;background:linear-gradient(#fff,var(--grid-bg))}
.card{position:absolute;width:275px}
.card-frame{width:275px;height:172px;background:#fff;padding:9px;box-shadow:0 2px 6px rgba(0,0,0,.28)}
.card-art{width:100%;height:100%}
.card h3{margin:18px 0 0 10px;font-size:18px;line-height:22px;font-weight:700;width:250px}
.card p{margin:14px 0 0 10px;width:250px;font-size:12.5px;line-height:16px;color:var(--body-text)}
.card a{display:block;margin:11px 0 0 10px;font-size:12.5px;color:var(--link-blue);text-decoration:none}

/* testimonial */
.testimonial{left:0;top:1828px;width:1200px;height:222px;background:#fff;border-top:1px solid #e2e2e2}
.quote-mark{position:absolute;left:134px;top:26px;font-family:"Gelasio",Georgia,serif;font-size:54px;line-height:54px;color:#d8d8d8}
.quote-label{position:absolute;left:173px;top:44px;font-size:10.5px;font-weight:700}
.quote-text{position:absolute;left:172px;top:70px;width:580px;font-family:"Gelasio",Georgia,serif;font-style:italic;font-size:19.5px;line-height:30px;color:#8c8c8c}
.quote-author{position:absolute;right:472px;top:173px;font-size:11px;font-weight:700}
.quote-author .name{color:var(--accent-orange)}
.video{position:absolute;left:807px;top:27px;width:260px;height:145px;background:#111;box-shadow:0 2px 6px rgba(0,0,0,.3)}
.video-bar{position:absolute;left:0;bottom:0;width:100%;height:16px;background:#0c0c0c;display:flex;align-items:center;gap:8px;padding:0 8px;font-size:8px;color:#ccc}
.video-track{flex:1;height:3px;background:#444}
.video-caption{position:absolute;left:808px;top:194px;font-size:15px;font-weight:700}

/* call to action */
.cta{left:0;top:2066px;width:1200px;height:72px;background:repeating-linear-gradient(135deg,#f3f5f7 0 3px,#eaeef2 3px 5px);border-top:1px solid #d7dde3;border-bottom:1px solid #d7dde3}
.cta p{position:absolute;left:119px;top:23px;font-size:21.5px;font-weight:700;color:#222}
.btn-enquiry{position:absolute;left:931px;top:16px;width:153px;height:38px;border-radius:19px;background:linear-gradient(#2a87dc,#0f56ad);border:2px solid #0d3f80;color:#fff;font-size:18px;font-weight:700;display:flex;align-items:center;justify-content:center}

/* footer */
.site-footer{left:0;top:2158px;width:1200px;height:81px;background:var(--footer-bg)}
.footer-brand{position:absolute;left:119px;top:32px;display:flex;align-items:center;gap:5px}
.footer-brand .brand-mark{width:12px;height:12px;background:#9aa}
.footer-brand span.name{font-size:14px;font-weight:700;color:#ccc}
.copyright{position:absolute;left:221px;top:34px;font-size:12px;color:#ddd}
.legal{position:absolute;right:116px;top:34px;font-size:12px;color:#4aa3e6}
.legal span{color:#ccc;padding:0 6px}
</style>
</head>
<body>

<header class="abs site-header">
  <div class="abs brand"><span class="brand-mark"></span><span class="brand-name">Frame KV</span></div>
  <nav class="abs util-links"><a href="#">Support</a><a href="#">Client Portal</a><a href="#">Contact</a><a href="#">About</a></nav>
  <div class="abs social" aria-label="Social links"><span></span><span></span><span></span></div>
  <div class="abs call">
    <span class="call-label">CALL US</span>
    <svg width="30" height="30" viewBox="0 0 30 30" aria-hidden="true"><circle cx="15" cy="15" r="15" fill="#2d8fd6"/><path d="M11 8c1 0 2 3 2 4s-1.5 1.2-1 2.5 2.5 3.5 3.5 4 1.5-1 2.5-1 4 1 4 2-2 3-4 3c-4 0-10-7-10-11 0-2 2-3.5 3-3.5z" fill="#fff"/></svg>
    <span class="call-number">1300 555 018</span>
  </div>
  <div class="abs search">Search
    <svg width="14" height="14" viewBox="0 0 14 14" aria-hidden="true"><circle cx="5.5" cy="5.5" r="4" fill="none" stroke="#fff" stroke-width="2"/><line x1="8.5" y1="8.5" x2="13" y2="13" stroke="#fff" stroke-width="2"/></svg>
  </div>
</header>

<nav class="abs main-nav">
  <a href="#" style="width:105px">What we do</a>
  <a href="#" style="width:148px">Builder Packages</a>
  <a href="#" style="width:113px">How it works</a>
  <a href="#" style="width:151px">Site Quarry</a>
  <a href="#" style="width:140px">Support Network</a>
  <a href="#" style="width:94px">Our Work</a>
  <a href="#" style="width:93px">Free trial</a>
</nav>

<section class="abs hero">
  <div class="abs shot" role="img" aria-label="Website screenshot of a sports club site" style="left:176px;top:72px;width:152px;height:210px;background:linear-gradient(#1e1e1e 0 8%,#3b3b3b 8% 30%,#d9d9d9 30% 34%,#2a2a2a 34% 55%,#eeeeee 55%)"></div>
  <div class="abs shot" role="img" aria-label="Website screenshot promoting responsive web design" style="left:328px;top:41px;width:241px;height:249px;background:linear-gradient(#3a3a3a 0 4%,#3aa6e0 4% 42%,#f5f5f5 42% 90%,#e3eef7 90%)"></div>
  <div class="abs shot" role="img" aria-label="Website screenshot of a search marketing page" style="left:569px;top:78px;width:127px;height:199px;background:linear-gradient(#e6eef5 0 30%,#f7f7f7 30% 70%,#dfe8f0 70%)"></div>
  <h1 class="abs hero-title">All in one Business<br>Solutions for Builders</h1>
  <p class="abs hero-copy">Lorem ipsum dolor sit amet consectetuer adipiscing elit nunc ullamcorper blandit urna. Sed facilisis accumsan nisi. Ut mattis libero quis sapien. Integer fermentum</p>
  <a class="abs btn-learn">Learn More</a>
  <div class="abs dots"><span></span><span class="on"></span><span></span><span></span><span></span></div>
</section>

<section class="abs intro">
  <h2>What we do?</h2>
  <p>Epsum factorial non deposit quid pro quo hic escorol. Olypian quarrels et gorilla congolium sic ad nauseum. Souvlaki ignitus arborund um e plurib Epsum factorial quarrels et gorilla congolium sic ad nauseum. Epsum factorial non deposit quid pro quo hic escorol.</p>
</section>

<section class="abs services">
  <article class="card" style="left:118px;top:42px">
    <div class="card-frame"><div class="card-art" role="img" aria-label="Grid of social media icons" style="background:radial-gradient(circle at 30% 40%,#9cc3e6,#d7e6f3 55%,#eef3f8)"></div></div>
    <h3>Online Marketing &amp; Social Media</h3>
    <p>Lorem ipsum dolor sit amet consectetuer adipiscing elit nunc ullamcorper blandit urna. Sed facilisis accumsan nisi. Ut mattis libero quis sapien. Integer fermentum venenatis</p>
    <a href="#">Read more&gt;&gt;</a>
  </article>
  <article class="card" style="left:463px;top:42px">
    <div class="card-frame"><div class="card-art" role="img" aria-label="Photo of a bright living room with a teal wall" style="background:linear-gradient(180deg,rgba(255,255,255,0) 70%,#d8d4cc 70%),linear-gradient(90deg,#ece9e3 55%,#1f8f9c 55%)"></div></div>
    <h3>Completely Rebrandable House Plans</h3>
    <p>Lorem ipsum dolor sit amet consectetuer adipiscing elit nunc ullamcorper blandit urna. Sed facilisis accumsan nisi. Ut mattis libero quis sapien. Integer fermentum venenatis</p>
    <a href="#">Read more&gt;&gt;</a>
  </article>
  <article class="card" style="left:807px;top:42px">
    <div class="card-frame"><div class="card-art" role="img" aria-label="Photo of construction tools, a hard hat and a calculator" style="background:radial-gradient(ellipse at 60% 55%,#6a6a6a,#b9b5ac 35%,#e4e4e4 70%)"></div></div>
    <h3>Construction Estimating Software</h3>
    <p>Lorem ipsum dolor sit amet consectetuer adipiscing elit nunc ullamcorper blandit urna. Sed facilisis accumsan nisi. Ut mattis libero quis sapien. Integer fermentum venenatis</p>
    <a href="#">Read more&gt;&gt;</a>
  </article>

  <article class="card" style="left:118px;top:406px">
    <div class="card-frame"><div class="card-art" role="img" aria-label="Photo of a support team member wearing a headset" style="background:linear-gradient(90deg,#d2a98e,#a9826b 40%,#5a4b44 70%,#2e2a2a)"></div></div>
    <h3>Awesome Support 24/7</h3>
    <p>Lorem ipsum dolor sit amet consectetuer adipiscing elit nunc ullamcorper blandit urna. Sed facilisis accumsan nisi. Ut mattis libero quis sapien. Integer fermentum venenatis</p>
    <a href="#">Read more&gt;&gt;</a>
  </article>
  <article class="card" style="left:463px;top:406px">
    <div class="card-frame"><div class="card-art" role="img" aria-label="Illustration of a web app on tablet and phone screens" style="background:linear-gradient(#7fc4d8 0 22%,#efe7c9 22% 90%,#d9ccaa 90%)"></div></div>
    <h3>Websites &amp; Zentap Apps</h3>
    <p>Lorem ipsum dolor sit amet consectetuer adipiscing elit nunc ullamcorper blandit urna. Sed facilisis accumsan nisi. Ut mattis libero quis sapien. Integer fermentum venenatis</p>
    <a href="#">Read more&gt;&gt;</a>
  </article>
  <article class="card" style="left:807px;top:406px">
    <div class="card-frame"><div class="card-art" role="img" aria-label="Photo of black and white business stationery" style="background:linear-gradient(120deg,#111 40%,#444 47%,#d9d9d9 52%,#c8c8c8)"></div></div>
    <h3>Branding &amp; Logos</h3>
    <p>Lorem ipsum dolor sit amet consectetuer adipiscing elit nunc ullamcorper blandit urna. Sed facilisis accumsan nisi. Ut mattis libero quis sapien. Integer fermentum venenatis</p>
    <a href="#">Read more&gt;&gt;</a>
  </article>

  <article class="card" style="left:118px;top:753px">
    <div class="card-frame"><div class="card-art" role="img" aria-label="Coloured house floor plan drawing" style="background:radial-gradient(ellipse at 40% 55%,#c99a72,#d8c3ad 40%,#e9e8ea 60%,#fafafa)"></div></div>
    <h3>Planning and Building Design</h3>
    <p>Lorem ipsum dolor sit amet consectetuer adipiscing elit nunc ullamcorper blandit urna. Sed facilisis accumsan nisi. Ut mattis libero quis sapien. Integer fermentum venenatis</p>
    <a href="#">Read more&gt;&gt;</a>
  </article>
  <article class="card" style="left:463px;top:753px">
    <div class="card-frame"><div class="card-art" role="img" aria-label="3D rendering of a modern house at dusk" style="background:linear-gradient(#6f8aa6,#b7c3cc 40%,#8d8a80 58%,#4d5a3c 75%,#3f6a2c)"></div></div>
    <h3>3d Visualisation<br>&amp; Rendering</h3>
    <p>Lorem ipsum dolor sit amet consectetuer adipiscing elit nunc ullamcorper blandit urna. Sed facilisis accumsan nisi. Ut mattis libero quis sapien. Integer fermentum venenatis</p>
    <a href="#">Read more&gt;&gt;</a>
  </article>
</section>

<section class="abs testimonial">
  <span class="quote-mark">“</span>
  <h4 class="quote-label">WHAT OTHERS SAY ABOUT US:</h4>
  <blockquote class="quote-text">Over the last eighteen months our sales have increased three-fold since the launch of our new web site. Coupled with the sheer speed of their delivery, it has made us delighted we chose Frame KV.</blockquote>
  <p class="quote-author"><span class="name">HAROLD PEMBERTON,</span>&nbsp; FOUNDER RIDGELINE APP CO</p>
  <div class="video">
    <div role="img" aria-label="Video still of a small modern house" style="position:absolute;left:0;top:0;width:100%;height:129px;background:linear-gradient(#8fb3cf,#cfd9de 45%,#9a9a90 62%,#5f7a45)"></div>
    <div class="video-bar">
      <svg width="7" height="8" viewBox="0 0 7 8" aria-hidden="true"><path d="M0 0l7 4-7 4z" fill="#ddd"/></svg>
      <span>3:19 / 7:00</span><span class="video-track"></span>
    </div>
  </div>
  <p class="video-caption">Watch this video on your website</p>
</section>

<section class="abs cta">
  <p>I’m interested in giving my business the competitive edge</p>
  <a class="btn-enquiry">Send Enquiry</a>
</section>

<footer class="abs site-footer">
  <div class="footer-brand"><span class="brand-mark"></span><span class="name">Frame KV</span></div>
  <p class="copyright">© Copyright 2012 Frame KV , All Rights Reserved</p>
  <p class="legal">Terms and Conditions<span>|</span>Sitemap<span>|</span>Privacy Policy</p>
</footer>

</body>
</html>
```